Corporate Business card, Letter head, & Envelope
CorvaneLG
Professional
Nadia Perrow
CEO
5827 Fenwillow Dr, Suite 408
Brenfield, Texas 75099
nadiap@corvaneloftsgroup.example
www.corvaneloftsgroup.example
We are a corporate travel management and not a leisure company, so we need to stay professional

```html
<!DOCTYPE html>
<html lang="en">
<head>
<meta charset="utf-8">
<title>CorvaneLG Business Card</title>
<link rel="stylesheet" href="https://fonts.googleapis.com/css2?family=Open+Sans:wght@400;600;700&display=swap">
<style>
  :root {
    --bg: #e9eaeb;
    --card: #ffffff;
    --navy: #1c4d9b;
    --blue: #2a63c4;
    --blue-deep: #163f8a;
    --blue-light: #6f9be0;
    --orange: #f39a1e;
    --ink: #2b2b2b;
    --rule: #d3d6db;
  }
  * { margin: 0; padding: 0; box-sizing: border-box; }
  html, body { width: 1200px; height: 898px; overflow: hidden; }
  body {
    background: var(--bg);
    font-family: "Open Sans", Arial, sans-serif;
    position: relative;
  }
  .card {
    position: absolute;
    left: 180px; top: 209px;
    width: 840px; height: 480px;
    background: var(--card);
    box-shadow: 0 10px 30px rgba(0,0,0,0.18);
    overflow: hidden;
  }
  .card-wave { position: absolute; left: 0; top: 0; width: 840px; height: 480px; }
  .brand {
    position: absolute; left: 70px; top: 140px;
    display: flex; align-items: center; gap: 18px;
  }
  .brand-mark { width: 58px; height: 58px; border-radius: 50%; background: var(--blue); }
  .brand-name { font-size: 42px; font-weight: 700; color: var(--navy); letter-spacing: 0.5px; }
  .divider {
    position: absolute; left: 470px; top: 62px;
    width: 1px; height: 240px; background: var(--rule);
  }
  .contact { position: absolute; left: 496px; top: 60px; color: var(--ink); }
  .contact-name { font-size: 26px; font-weight: 700; color: var(--navy); line-height: 1.1; }
  .contact-role { font-size: 15px; font-weight: 600; color: var(--navy); margin-bottom: 14px; }
  .contact-address { font-size: 14px; line-height: 1.45; margin-bottom: 14px; }
  .contact-list { list-style: none; font-size: 14px; line-height: 1.6; }
  .contact-list li { display: flex; align-items: center; gap: 10px; }
  .contact-list svg { width: 14px; height: 14px; flex: none; }
  .contact-tollfree { font-size: 14px; margin-top: 14px; }
  .tagline {
    position: absolute; left: 42px; top: 418px;
    font-size: 21px; color: #ffffff; letter-spacing: 0.3px;
  }
</style>
</head>
<body>
  <div class="card">
    <svg class="card-wave" viewBox="0 0 840 480" aria-hidden="true">
      <defs>
        <linearGradient id="band" x1="0" y1="0" x2="1" y2="0">
          <stop offset="0" stop-color="#2f6fd0"/>
          <stop offset="1" stop-color="#163f8a"/>
        </linearGradient>
      </defs>
      <path d="M0 378 C 260 360 600 350 840 296 L840 314 C 580 366 260 376 0 392 Z" fill="var(--blue-light)"/>
      <path d="M420 362 C 600 350 720 330 840 282 L840 306 C 720 346 600 356 420 366 Z" fill="var(--orange)"/>
      <path d="M0 394 C 260 378 580 368 840 312 L840 480 L0 480 Z" fill="url(#band)"/>
    </svg>

    <div class="brand">
      <span class="brand-mark"></span>
      <span class="brand-name">CorvaneLG</span>
    </div>

    <div class="divider"></div>

    <div class="contact">
      <p class="contact-name">Nadia Perrow</p>
      <p class="contact-role">CEO</p>
      <p class="contact-address">5827 Fenwillow Dr, Suite 408<br>Brenfield, Texas 75099</p>
      <ul class="contact-list">
        <li><svg viewBox="0 0 14 14"><path d="M3 1 L5 1 L6 4 L4.5 5.5 C5.5 7.5 6.5 8.5 8.5 9.5 L10 8 L13 9 L13 11 C13 12 12 13 11 13 C6 13 1 8 1 3 C1 2 2 1 3 1 Z" fill="var(--navy)"/></svg>972-555-0140</li>
        <li><svg viewBox="0 0 14 14"><rect x="1" y="4" width="12" height="8" rx="1" fill="var(--navy)"/><rect x="3" y="2" width="8" height="3" fill="var(--navy)"/></svg>972-555-0168</li>
        <li><svg viewBox="0 0 14 14"><rect x="1" y="3" width="12" height="8" fill="var(--navy)"/><path d="M1 3 L7 8 L13 3" stroke="#fff" stroke-width="1" fill="none"/></svg>nadiap@corvaneloftsgroup.example</li>
        <li><svg viewBox="0 0 14 14"><circle cx="7" cy="7" r="6" fill="none" stroke="var(--navy)" stroke-width="1.3"/><path d="M1 7 H13 M7 1 C4 4 4 10 7 13 M7 1 C10 4 10 10 7 13" stroke="var(--navy)" stroke-width="1" fill="none"/></svg>www.corvaneloftsgroup.example</li>
      </ul>
      <p class="contact-tollfree">Toll Free 800-555-0193</p>
    </div>

    <p class="tagline">corporate travel management</p>
  </div>
</body>
</html>
```